Fernvale Accounting - New Postcard for B2B marketing

I need a postcard for my business that provides cloud-based bookkeeping services with LedgerCloud Online. Our clients are small independently owned businesses. Please use our website for inspiration (colors, content, etc)... www.FernvaleAccounting.com.

Target Market(s)

Small, independently-owned businesses, including restaurants, retail stores, small medical practices, etc

Industry/Entity Type

Bookkeeper

Font styles to use
Serif

Colors
3276b5
155ea9
c4d6e9
85cae6
33a6d7

Requirements
Must have
• Must have my logo (see attached), business contact info (see website), description of services, blue color scheme
Nice to have
• Maybe add "Prices starting at $750/mo"
Content should match info on our website
4 x 6 horizontal postcard (see attached template)

```html
<!DOCTYPE html>
<html lang="en">
<head>
<meta charset="utf-8">
<title>Fernvale Accounting – Postcard Concepts</title>
<link rel="stylesheet" href="https://fonts.googleapis.com/css2?family=Merriweather:wght@400;700;900&family=Bitter:wght@700&family=Montserrat:wght@600;800&family=Oswald:wght@500&display=swap">
<style>
  :root{
    --board:#c8c8c8;
    --navy:#1a3f74;
    --navy-deep:#163563;
    --blue:#155ea9;
    --blue-mid:#3276b5;
    --sky:#33a6d7;
    --aqua:#3fb6d1;
    --pale:#c4d6e9;
    --ice:#e8eef5;
    --green:#3aa64a;
    --white:#ffffff;
    --badge:#d9e2ea;
  }
  *{box-sizing:border-box;margin:0;padding:0}
  html,body{width:866px;height:1200px;overflow:hidden;background:var(--board)}
  .card{position:absolute;left:61px;width:736px;height:491px;background:var(--white);overflow:hidden;font-family:"Merriweather",Georgia,serif}
  .card--classic{top:71px}
  .card--modern{top:624px}
  .abs{position:absolute}

  .wordmark{position:absolute;color:var(--navy);font-family:"Merriweather",Georgia,serif;font-weight:700;line-height:1}
  .wordmark__name{display:block;font-size:50px;letter-spacing:1px}
  .wordmark__sub{display:block;font-size:22px;margin-top:8px;letter-spacing:.5px}

  .tagline{font-family:"Bitter",Georgia,serif;font-weight:700;color:var(--blue);font-size:18.5px;line-height:21px}
  .partner-mark{position:absolute;border-radius:50%}
  .partner-mark--green{background:var(--green)}
  .badge{position:absolute;border-radius:50%;background:var(--badge);border:3px solid #c9a860}
  .social{position:absolute;border-radius:50%;background:var(--sky)}
  .follow{position:absolute;font-family:"Merriweather",Georgia,serif;font-weight:700;font-size:9px}

  /* classic card */
  .classic__band{left:0;top:120px;width:736px;height:224px;background:var(--navy)}
  .classic__photo{left:300px;top:120px;width:436px;height:224px;background:linear-gradient(90deg,var(--navy) 0%,#3e6294 25%,#9fb3cb 60%,#d7e0ea 100%)}
  .classic__headline{left:40px;top:131px;color:var(--white);font-family:"Merriweather",Georgia,serif;font-weight:900;font-size:42px;line-height:40px;letter-spacing:.5px}
  .classic__strip{left:0;top:344px;width:736px;height:58px;background:linear-gradient(90deg,var(--blue) 0%,var(--blue-mid) 100%)}
  .classic__laptop{left:0;top:272px;width:300px;height:153px;background:linear-gradient(180deg,#2a2a2e 0%,#dfe6ee 10%,#f4f7fa 80%,#b8bcc2 100%);border-radius:6px 6px 2px 2px}
  .quote-disc{left:285px;top:283px;width:128px;height:128px;border-radius:50%;background:var(--aqua);color:var(--white);display:flex;align-items:center;justify-content:center;text-align:center;font-family:"Merriweather",Georgia,serif;font-weight:700;font-size:15px;line-height:21.5px}
  .classic__phone{left:462px;top:346px;color:var(--white);font-family:"Merriweather",Georgia,serif;font-weight:900;font-size:34px;line-height:52px;letter-spacing:.5px}
  .classic__contact{left:50px;top:435px;color:var(--navy);font-family:"Merriweather",Georgia,serif;font-weight:700;font-size:15px;line-height:19px}
  .contact-line{display:flex;align-items:center;gap:8px;white-space:nowrap}

  /* modern card */
  .modern__bg{inset:0;background:linear-gradient(180deg,#dfe7f0 0%,#eef2f7 45%,#e3eaf2 100%)}
  .modern__headline{left:31px;top:145px;color:var(--navy);font-family:"Montserrat",Arial,sans-serif;line-height:43px;font-size:41px}
  .modern__headline b{font-weight:800;display:block}
  .modern__headline span{font-weight:600;display:block}
  .band-title{font-family:"Oswald",Arial,sans-serif;font-weight:500;color:var(--white);font-size:27px;line-height:37px}
  .modern__service{left:41px;top:295px}
  .modern__service-right{left:430px;top:291px;width:306px;height:53px;color:var(--white);text-align:center;font-family:"Merriweather",Georgia,serif;font-weight:700;font-size:19px;line-height:18px;padding-top:8px;letter-spacing:.5px}
  .modern__copy{left:164px;top:353px;color:var(--navy);font-family:"Merriweather",Georgia,serif;font-size:15px;line-height:20px}
  .modern__footer{left:0;top:427px;width:736px;height:64px;background:var(--navy)}
  .modern__tab{left:0;top:416px;width:168px;height:75px;background:var(--aqua);border-radius:0 22px 0 0;color:var(--white);text-align:center;font-family:"Merriweather",Georgia,serif;font-weight:700;font-size:15.5px;line-height:18px;padding-top:11px;white-space:nowrap}
  .modern__phone{left:224px;top:434px;color:var(--white);font-family:"Oswald",Arial,sans-serif;font-weight:500;font-size:30px;line-height:50px;letter-spacing:-1.2px;white-space:nowrap}
  .modern__contact{left:402px;top:440px;color:var(--white);font-family:"Merriweather",Georgia,serif;font-size:14px;line-height:19px}
</style>
</head>
<body>

<section class="card card--classic">
  <div class="wordmark" style="left:52px;top:26px">
    <span class="wordmark__name">Fernvale</span>
    <span class="wordmark__sub">Accounting</span>
  </div>
  <p class="abs tagline" style="left:358px;top:23px">Specializing in Cloud-Based<br>Bookkeeping &amp; Payroll<br>Processing with LedgerCloud<br>Online by Nimbus.</p>
  <div class="partner-mark partner-mark--green" style="left:640px;top:29px;width:61px;height:61px"></div>

  <div class="abs classic__band"></div>
  <div class="abs classic__photo" role="img" aria-label="Photo of hands writing in a notebook beside a calculator"></div>
  <h1 class="abs classic__headline">ACCOUNTING<br>FOR YOUR<br>BUSINESS</h1>
  <div class="abs classic__strip"></div>
  <div class="abs classic__laptop" role="img" aria-label="Laptop showing a cloud bookkeeping dashboard"></div>
  <div class="abs quote-disc">REQUEST<br>YOUR FREE<br>QUOTE<br>TODAY!</div>
  <svg class="abs" style="left:423px;top:357px" width="32" height="34" viewBox="0 0 32 34" aria-hidden="true">
    <rect x="9" y="2" width="16" height="30" rx="3" fill="none" stroke="#fff" stroke-width="2.5"/>
    <path d="M2 10 q-3 8 2 16" fill="none" stroke="#fff" stroke-width="3" stroke-linecap="round"/>
    <circle cx="17" cy="27" r="1.6" fill="#fff"/>
  </svg>
  <div class="abs classic__phone">555.014.0199</div>

  <div class="abs classic__contact">
    <div class="contact-line">
      <svg width="16" height="14" viewBox="0 0 16 14" aria-hidden="true"><rect x="1" y="2" width="14" height="10" fill="none" stroke="#3276b5" stroke-width="1.6"/><path d="M1 2 L8 8 L15 2" fill="none" stroke="#3276b5" stroke-width="1.6"/></svg>
      info@fernvaleaccounting.com
    </div>
    <div class="contact-line">
      <svg width="16" height="16" viewBox="0 0 16 16" aria-hidden="true"><circle cx="8" cy="8" r="6.5" fill="none" stroke="#3276b5" stroke-width="1.6"/><path d="M1.5 8 H14.5 M8 1.5 C4 5 4 11 8 14.5 C12 11 12 5 8 1.5" fill="none" stroke="#3276b5" stroke-width="1.2"/></svg>
      www.FernvaleAccounting.com
    </div>
  </div>

  <div class="badge" style="left:401px;top:412px;width:64px;height:64px;border-color:#9aa7b2"></div>
  <div class="badge" style="left:485px;top:412px;width:66px;height:66px"></div>
  <div class="badge" style="left:573px;top:412px;width:66px;height:66px"></div>
  <div class="follow" style="left:663px;top:436px;color:#111">Follow Us</div>
  <div class="social" style="left:657px;top:452px;width:23px;height:23px"></div>
  <div class="social" style="left:687px;top:452px;width:23px;height:23px"></div>
</section>

<section class="card card--modern">
  <div class="abs modern__bg" role="img" aria-label="Faint city skyline photo behind the headline"></div>

  <svg class="abs" style="left:0;top:0" width="736" height="491" viewBox="0 0 736 491" aria-hidden="true">
    <polygon points="350,0 736,0 736,288 431,288" fill="#7f8e9e"/>
    <polygon points="316,0 334,0 460,427 442,427" fill="#33a6d7"/>
    <polygon points="334,0 352,0 478,427 460,427" fill="#1a3f74"/>
    <polygon points="432,291 736,291 736,344 447,344" fill="#1a3f74"/>
    <polygon points="447,344 736,344 736,427 470,427" fill="#ffffff"/>
    <polygon points="0,295 398,295 410,332 0,332" fill="#1a3f74"/>
    <polygon points="398,295 408,295 420,332 410,332" fill="#33a6d7"/>
  </svg>
  <div class="abs" style="left:350px;top:0;width:386px;height:288px;clip-path:polygon(0 0,100% 0,100% 100%,21% 100%);background:linear-gradient(135deg,#6f5a48 0%,#cfd6de 30%,#f2f4f7 60%,#8d9aa8 100%)" role="img" aria-label="Photo of a laptop displaying a cloud bookkeeping dashboard"></div>

  <div class="wordmark" style="left:45px;top:32px">
    <span class="wordmark__name">Fernvale</span>
    <span class="wordmark__sub">Accounting</span>
  </div>

  <h2 class="abs modern__headline"><b>ACCOUNTING</b><span>FOR YOUR</span><span>BUSINESS</span></h2>

  <div class="abs band-title modern__service">FULL SERVICE BOOKKEEPING</div>
  <div class="abs modern__service-right">FULL SERVICE<br>BOOKKEEPING</div>

  <div class="partner-mark partner-mark--green" style="left:27px;top:347px;width:60px;height:60px"></div>
  <p class="abs modern__copy">Specializing in Cloud-Based<br>Bookkeeping &amp; Payroll Processing<br>with LedgerCloud Online by Nimbus.</p>

  <div class="badge" style="left:483px;top:354px;width:64px;height:64px;border-color:#9aa7b2"></div>
  <div class="badge" style="left:564px;top:353px;width:66px;height:66px"></div>
  <div class="badge" style="left:642px;top:353px;width:66px;height:66px"></div>

  <div class="abs modern__footer"></div>
  <div class="abs modern__tab">REQUEST<br>A FREE QUOTE<br>TODAY!</div>
  <svg class="abs" style="left:186px;top:443px" width="32" height="34" viewBox="0 0 32 34" aria-hidden="true">
    <rect x="9" y="2" width="16" height="30" rx="3" fill="none" stroke="#fff" stroke-width="2.5"/>
    <path d="M2 10 q-3 8 2 16" fill="none" stroke="#fff" stroke-width="3" stroke-linecap="round"/>
    <circle cx="17" cy="27" r="1.6" fill="#fff"/>
  </svg>
  <div class="abs modern__phone">555.014.0199</div>
  <div class="abs modern__contact">
    <div class="contact-line">
      <svg width="12" height="11" viewBox="0 0 16 14" aria-hidden="true"><rect x="1" y="2" width="14" height="10" fill="none" stroke="#85cae6" stroke-width="1.6"/><path d="M1 2 L8 8 L15 2" fill="none" stroke="#85cae6" stroke-width="1.6"/></svg>
      info@fernvaleaccounting.com
    </div>
    <div class="contact-line">
      <svg width="12" height="12" viewBox="0 0 16 16" aria-hidden="true"><circle cx="8" cy="8" r="6.5" fill="none" stroke="#85cae6" stroke-width="1.6"/><path d="M1.5 8 H14.5 M8 1.5 C4 5 4 11 8 14.5 C12 11 12 5 8 1.5" fill="none" stroke="#85cae6" stroke-width="1.2"/></svg>
      www.FernvaleAccounting.com
    </div>
  </div>
  <div class="follow" style="left:674px;top:439px;color:#fff">Follow Us</div>
  <div class="social" style="left:670px;top:455px;width:20px;height:20px"></div>
  <div class="social" style="left:695px;top:455px;width:20px;height:20px"></div>
</section>

</body>
</html>
```